Business card design needed for a security services business.

We provide a wide range of security services from guard personnel to electronic systems.

Industry/Entity Type

Security Industry

Contact Information for Business Card

Brent Holloway, Owner Office: 780.555.0148; Cell: 780.555.0193 Email: brent@norcrestwatchgroup.example; Address 20487 163 St Edmonton, AB T5X 2K8

Colors
0054AA
0677BA
7BADD7
CADEEF
E8F1F8

Requirements
Nice to have
• On the back of the card I would like to possible list the services I provide: Guards Mobiles Live Video Surveillance Access Intrusion

```html
<!DOCTYPE html>
<html lang="en">
<head>
<meta charset="utf-8">
<title>Norcrest Watch Group – Business Card</title>
<link rel="stylesheet" href="https://fonts.googleapis.com/css2?family=Lato:wght@400;700;900&display=swap">
<style>
  :root {
    --stage: #474747;
    --card: #171717;
    --blue: #0f5bb5;
    --blue-deep: #0054aa;
    --grey-line: #5e5e5e;
    --white: #ffffff;
  }
  * { box-sizing: border-box; margin: 0; padding: 0; }
  html, body { width: 1200px; height: 801px; overflow: hidden; }
  body {
    background: var(--stage);
    font-family: "Lato", sans-serif;
    display: flex;
    align-items: center;
    justify-content: center;
    gap: 50px;
  }
  .card {
    position: relative;
    width: 525px;
    height: 300px;
    background: var(--card);
    border-radius: 18px;
    border-left: 3px solid var(--blue);
    border-bottom: 3px solid var(--blue);
    overflow: hidden;
    color: var(--white);
  }

  /* Front: contact side */
  .card-front .corner-tab {
    position: absolute; top: 0; right: 40px;
    width: 30px; height: 34px; background: var(--blue);
  }
  .card-front .person {
    position: absolute; top: 44px; right: 40px; text-align: right;
  }
  .card-front .person-name {
    color: var(--blue); font-weight: 700; font-size: 25px; letter-spacing: 0.3px;
  }
  .card-front .person-role { font-size: 14px; margin-top: 2px; }
  .card-front .address {
    position: absolute; top: 150px; right: 40px; text-align: right;
    font-size: 14px; line-height: 1.45;
  }
  .card-front .brand {
    position: absolute; top: 110px; left: 34px; width: 230px;
  }
  .brand-name {
    display: flex; align-items: center; gap: 10px;
    color: var(--blue); font-weight: 900; font-size: 23px; line-height: 1.05;
    letter-spacing: 1px; text-transform: uppercase;
  }
  .brand-mark { width: 14px; height: 14px; background: var(--blue); flex: none; }
  .brand-rule { height: 1px; background: var(--grey-line); margin-top: 12px; }
  .card-front .contacts {
    position: absolute; left: 34px; bottom: 26px; list-style: none;
    font-size: 14px; line-height: 1.55;
  }
  .contacts li { display: flex; align-items: center; gap: 10px; }
  .contacts svg { width: 14px; height: 14px; flex: none; }

  /* Back: services side */
  .card-back { display: flex; flex-direction: column; align-items: center; padding-top: 70px; }
  .card-back .brand-name { font-size: 36px; gap: 14px; }
  .card-back .brand-mark { width: 20px; height: 20px; }
  .card-back .brand-rule { width: 400px; margin-top: 16px; }
  .services-pill {
    margin-top: 14px; background: var(--blue); color: var(--white);
    font-weight: 700; font-size: 22px; padding: 6px 24px; border-radius: 30px;
  }
  .services-list { margin-top: 14px; font-size: 14.5px; letter-spacing: 0.3px; }
</style>
</head>
<body>
  <section class="card card-front">
    <div class="corner-tab"></div>
    <div class="person">
      <div class="person-name">Brent Holloway</div>
      <div class="person-role">Owner</div>
    </div>
    <div class="address">20487 163 St Edmonton,<br>AB T5X 2K8</div>

    <div class="brand">
      <div class="brand-name"><span class="brand-mark"></span><span>Norcrest Watch Group</span></div>
      <div class="brand-rule"></div>
    </div>

    <ul class="contacts">
      <li>
        <svg viewBox="0 0 16 16" aria-hidden="true"><path fill="#0f5bb5" d="M3 2h3l1.5 3.5-2 1.2a8 8 0 0 0 3.8 3.8l1.2-2L14 10v3a1 1 0 0 1-1 1A11 11 0 0 1 2 3a1 1 0 0 1 1-1z"/></svg>
        <span>780.555.0148</span>
      </li>
      <li>
        <svg viewBox="0 0 16 16" aria-hidden="true"><rect x="4" y="1" width="8" height="14" rx="1.5" fill="none" stroke="#0f5bb5" stroke-width="1.6"/></svg>
        <span>780.555.0193</span>
      </li>
      <li>
        <svg viewBox="0 0 16 16" aria-hidden="true"><rect x="1" y="3" width="14" height="10" fill="#0f5bb5"/><path d="M1 3l7 6 7-6" fill="none" stroke="#171717" stroke-width="1.4"/></svg>
        <span>brent@norcrestwatchgroup.example</span>
      </li>
    </ul>
  </section>

  <section class="card card-back">
    <div class="brand-name"><span class="brand-mark"></span><span>Norcrest Watch Group</span></div>
    <div class="brand-rule"></div>
    <div class="services-pill">services I provide</div>
    <p class="services-list">Guards Mobiles Live Video Surveillance Access Intrusion</p>
  </section>
</body>
</html>
```